Website for an interior designer

We need a new website for Clara Beth Holloway whose new business name is Clara Beth Holloway Interiors. She is a residential interior designer with a mix of modern and contemporary tastes. We are in the process of overhauling her website which is +15 years old and not an accurate reflection of her tastes. The uploaded photos are from some of the houses she has done as well as her logo(s). We would need a section for "About Us" that would have a paragraph of text and bullets showing services and a gallery for photos (~12 total, more to come). A contract page would be optional. The client likes the feel/look of this website: https://www.pondrickstudio.example/ but doesn't want to copy it exactly.

Target Market(s)

Upscale home owners

Industry/Entity Type

Interior Design

Coding

Coded - Design and coding required

Number of Pages Required

4 page

Colors

Designer to choose only greyscale colors for use in the design.

Requirements
Must have
• Home page, about us page, gallery page, contact us page.

```html
<!DOCTYPE html>
<html lang="en">
<head>
<meta charset="utf-8">
<title>Clara Beth Holloway Interiors</title>
<link href="https://fonts.googleapis.com/css2?family=Cinzel:wght@400;600&family=Open+Sans:wght@400;600&family=Poppins:wght@400&display=swap" rel="stylesheet">
<style>
:root{
  --ink:#1c1c1c;
  --text:#444;
  --muted:#777;
  --line:#e6e6e6;
  --paper:#ffffff;
  --dark:#1b1b1b;
  --on-dark:#f2f2f2;
  --on-dark-muted:#a9a9a9;
}
*{box-sizing:border-box;margin:0;padding:0}
html,body{width:1200px;height:2700px;overflow:hidden}
body{position:relative;background:var(--paper);color:var(--text);font-family:"Open Sans",sans-serif}
.abs{position:absolute}
.serif{font-family:"Cinzel",serif}
a{color:inherit;text-decoration:none}

/* header */
.brand{left:38px;top:18px;width:162px;text-align:center}
.brand-mark{font-family:"Cinzel",serif;font-size:26px;color:var(--ink);line-height:1}
.brand-name{font-family:"Cinzel",serif;font-size:11px;color:var(--ink);letter-spacing:.5px;margin-top:8px;white-space:nowrap}
.brand-sub{font-family:"Cinzel",serif;font-size:7px;letter-spacing:3px;color:var(--ink);margin-top:3px}
.nav{left:445px;top:37px;display:flex;gap:25px;font-size:11.5px;color:var(--ink);letter-spacing:.3px}
.nav .active{border-bottom:1px solid var(--ink);padding-bottom:3px}
.phone-btn{display:flex;align-items:center;justify-content:center;gap:9px;border:2px solid var(--ink);font-family:"Cinzel",serif;color:var(--ink)}
.header-phone{left:999px;top:23px;width:161px;height:43px;font-size:16px;font-weight:600}

/* hero */
.hero{left:38px;top:90px;width:1124px;height:622px;background:linear-gradient(180deg,#e9e7e3 0%,#dcd8d2 55%,#9d958a 100%)}
.hero-title{left:38px;top:328px;width:1124px;text-align:center;font-family:"Cinzel",serif;font-weight:600;font-size:38px;line-height:45px;color:var(--ink)}
.hero-sub{left:38px;top:424px;width:1124px;text-align:center;font-family:"Poppins",sans-serif;font-size:14px;color:#2a2a2a}
.dots{left:546px;top:683px;display:flex;gap:9px}
.dots span{width:11px;height:11px;border-radius:50%;background:#fff}

/* section headings */
.eyebrow{width:1200px;left:0;text-align:center;font-size:12.5px;letter-spacing:.5px;color:#555}
.section-title{width:1200px;left:0;text-align:center;font-family:"Cinzel",serif;font-weight:600;font-size:33px;color:var(--ink)}

/* services */
.services-bg{left:0;top:838px;width:1200px;height:460px;background:linear-gradient(180deg,#fff 0%,#f3f2f0 30%,#eeecea 70%,#fff 100%)}
.service{width:190px;text-align:center;font-size:12px;line-height:18px;color:#3a3a3a}
.service .ring{display:block;margin:0 auto 10px;width:76px;height:76px}

/* about */
.about-panel{left:510px;top:1274px;width:690px;height:473px;background:var(--dark)}
.about-photo{left:193px;top:1342px;width:416px;height:338px;background:linear-gradient(160deg,#f1eee9 0%,#d9d3ca 50%,#8f8474 100%)}
.about-eyebrow{left:675px;top:1386px;font-size:13px;color:var(--on-dark)}
.about-title{left:673px;top:1411px;font-family:"Cinzel",serif;font-size:31px;line-height:37px;color:var(--on-dark)}
.about-text{left:675px;top:1498px;width:345px;font-size:10.5px;line-height:21px;color:var(--on-dark-muted)}
.about-btn{left:676px;top:1642px;width:124px;height:38px;border:1px solid var(--on-dark);color:var(--on-dark);font-family:"Cinzel",serif;font-size:13px;display:flex;align-items:center;justify-content:center}

/* gallery */
.tile{width:255px;height:262px}
.tile-entry{left:195px;top:1913px;background:linear-gradient(120deg,#f4f4f2 0%,#dedcd8 60%,#8e8c86 100%)}
.tile-kitchen{left:473px;top:1913px;background:linear-gradient(180deg,#eeeeec 0%,#d8d8d6 60%,#a27b5a 100%)}
.tile-living{left:750px;top:1913px;background:linear-gradient(180deg,#eae8e4 0%,#cfcac3 60%,#b9ab98 100%)}
.caption{width:210px;height:51px;border:1px solid var(--line);border-top:none;display:flex;align-items:center;justify-content:center;font-family:"Cinzel",serif;font-size:15px;color:#444;background:#fff}

/* contact */
.contact-mark{left:0;width:1200px;top:2300px;text-align:center;font-family:"Cinzel",serif;font-size:44px;color:var(--ink)}
.contact-text{left:0;width:1200px;top:2364px;text-align:center;font-size:20px;line-height:30px;color:#2a2a2a}
.contact-phone{left:521px;top:2437px;width:158px;height:42px;font-size:16px;font-weight:600}

/* footer */
.footer{left:0;top:2550px;width:1200px;height:150px;background:var(--dark)}
.footer-brand{left:160px;top:2600px;width:162px;text-align:center;color:var(--on-dark)}
.footer-brand .brand-mark,.footer-brand .brand-name,.footer-brand .brand-sub{color:var(--on-dark)}
.footer-links{left:475px;top:2606px;font-size:10.5px;color:var(--on-dark-muted);word-spacing:2px}
.footer-copy{left:476px;top:2629px;font-size:10px;color:var(--on-dark-muted)}
.socials{left:937px;top:2632px;display:flex;gap:5px}
.socials span{width:30px;height:30px;border:1px solid var(--on-dark-muted);border-radius:50%}
</style>
</head>
<body>

<header>
  <div class="abs brand">
    <div class="brand-mark">CBH</div>
    <div class="brand-name">CLARA BETH HOLLOWAY</div>
    <div class="brand-sub">INTERIORS</div>
  </div>
  <nav class="abs nav">
    <a class="active">HOME</a><a>ABOUT</a><a>SERVICES</a><a>GALLERY</a><a>CONTACT</a>
  </nav>
  <a class="abs phone-btn header-phone">
    <svg width="16" height="16" viewBox="0 0 24 24"><path fill="#1c1c1c" d="M6.6 10.8c1.4 2.8 3.8 5.1 6.6 6.6l2.2-2.2c.3-.3.7-.4 1-.2 1.1.4 2.3.6 3.6.6.6 0 1 .4 1 1V20c0 .6-.4 1-1 1C10.6 21 3 13.4 3 4c0-.6.4-1 1-1h3.5c.6 0 1 .4 1 1 0 1.3.2 2.5.6 3.6.1.3 0 .7-.2 1z"/></svg>
    123 555 0148
  </a>
</header>

<section>
  <div class="abs hero" role="img" aria-label="Bright living room with grey sectional sofa, round wooden tables and woven pendant lamp"></div>
  <h1 class="abs hero-title">CLARA BETH HOLLOWAY<br>INTERIORS</h1>
  <p class="abs hero-sub">Work In Residential And Commercial Projects</p>
  <div class="abs dots"><span></span><span></span><span></span><span></span></div>
</section>

<section>
  <div class="abs services-bg" role="img" aria-label="Faded photo of a light kitchen and dining room"></div>
  <p class="abs eyebrow" style="top:779px">WHAT WE DO</p>
  <h2 class="abs section-title" style="top:800px">OUR SERVICES</h2>

  <div class="abs service" style="left:282px;top:876px">
    <svg class="ring" viewBox="0 0 76 76"><circle cx="38" cy="38" r="37" fill="#fff" stroke="#333"/><path d="M28 48l18-18M44 26l6 6M30 42l4 4" stroke="#333" stroke-width="1.5" fill="none"/></svg>
    Concept Origination and Project Management
  </div>
  <div class="abs service" style="left:503px;top:876px">
    <svg class="ring" viewBox="0 0 76 76"><circle cx="38" cy="38" r="37" fill="#fff" stroke="#333"/><rect x="24" y="24" width="28" height="28" stroke="#333" stroke-width="1.5" fill="none"/><path d="M24 38h14v14" stroke="#333" stroke-width="1.5" fill="none"/></svg>
    Review of Proposed Plans for New Construction And Remodels
  </div>
  <div class="abs service" style="left:722px;top:876px">
    <svg class="ring" viewBox="0 0 76 76"><circle cx="38" cy="38" r="37" fill="#fff" stroke="#333"/><rect x="22" y="34" width="16" height="16" stroke="#333" stroke-width="1.5" fill="none"/><rect x="40" y="28" width="14" height="22" stroke="#333" stroke-width="1.5" fill="none"/></svg>
    Procurement of Furniture, Accents, Art, Fixtures and Fittings
  </div>
  <div class="abs service" style="left:282px;top:1065px">
    <svg class="ring" viewBox="0 0 76 76"><circle cx="38" cy="38" r="37" fill="#fff" stroke="#333"/><path d="M30 24h16v10H30zM38 34v18M32 52h12" stroke="#333" stroke-width="1.5" fill="none"/></svg>
    Selection of Paints, Finishes and Construction Materials
  </div>
  <div class="abs service" style="left:503px;top:1065px">
    <svg class="ring" viewBox="0 0 76 76"><circle cx="38" cy="38" r="37" fill="#fff" stroke="#333"/><rect x="28" y="22" width="22" height="30" stroke="#333" stroke-width="1.5" fill="none"/><circle cx="35" cy="46" r="5" stroke="#333" stroke-width="1.5" fill="none"/></svg>
    Vendor Coordination and Recommendations
  </div>
  <div class="abs service" style="left:722px;top:1065px">
    <svg class="ring" viewBox="0 0 76 76"><circle cx="38" cy="38" r="37" fill="#fff" stroke="#333"/><path d="M22 38l16-14 16 14M26 36v16h24V36" stroke="#333" stroke-width="1.5" fill="none"/></svg>
    Home Staging, Styling and Editing
  </div>
</section>

<section>
  <div class="abs about-panel"></div>
  <div class="abs about-photo" role="img" aria-label="Airy white living room with tall black-framed windows and cream sofas"></div>
  <p class="abs about-eyebrow">ABOUT US</p>
  <h2 class="abs about-title">CLARA BETH HOLLOWAY<br>INTERIORS</h2>
  <p class="abs about-text">Clara Beth Holloway has extensive experience in all aspects of interior design. She has worked on a wide array of residential and commercial projects in her hometown of Houston and across the United States. Clara Beth's taste can best be described as a sophisticated blend of modern and traditional styles that combine to create a clean, timeless space.</p>
  <a class="abs about-btn">LEARN MORE</a>
</section>

<section>
  <p class="abs eyebrow" style="top:1818px">WHAT WE DO</p>
  <h2 class="abs section-title" style="top:1838px">OUR GALLERY</h2>

  <div class="abs tile tile-entry" role="img" aria-label="Entry hall with white spiral staircase and tall window"></div>
  <div class="abs caption" style="left:217px;top:2175px">ENTRY</div>
  <div class="abs tile tile-kitchen" role="img" aria-label="White kitchen with steel refrigerator and wood floor"></div>
  <div class="abs caption" style="left:495px;top:2175px">KITCHEN</div>
  <div class="abs tile tile-living" role="img" aria-label="Living room with grey sofa, framed art and woven pendant"></div>
  <div class="abs caption" style="left:772px;top:2175px">LIVING ROOM</div>
</section>

<section>
  <div class="abs contact-mark">CBH</div>
  <p class="abs contact-text">If you Have an Any Question for<br>Contact us Today !</p>
  <a class="abs phone-btn contact-phone">
    <svg width="15" height="15" viewBox="0 0 24 24"><path fill="#1c1c1c" d="M6.6 10.8c1.4 2.8 3.8 5.1 6.6 6.6l2.2-2.2c.3-.3.7-.4 1-.2 1.1.4 2.3.6 3.6.6.6 0 1 .4 1 1V20c0 .6-.4 1-1 1C10.6 21 3 13.4 3 4c0-.6.4-1 1-1h3.5c.6 0 1 .4 1 1 0 1.3.2 2.5.6 3.6.1.3 0 .7-.2 1z"/></svg>
    123 555 0148
  </a>
</section>

<footer>
  <div class="abs footer"></div>
  <div class="abs footer-brand">
    <div class="brand-mark">CBH</div>
    <div class="brand-name">CLARA BETH HOLLOWAY</div>
    <div class="brand-sub">INTERIORS</div>
  </div>
  <p class="abs footer-links">Home | About | Services | Gallery | Contact</p>
  <p class="abs footer-copy">©Clara Beth Holloway - 2020 All Rights Reserved.</p>
  <div class="abs socials"><span></span><span></span><span></span></div>
</footer>

</body>
</html>
```